Maplecrest Apartments Downtown Northport

We are looking to redesign our entry way sign at Maplecrest Apartments, a low density residential apartment building, located in Downtown Northport, Alabama, U.S. Downtown Northport is a bustling boutique business district with a small town feel comprised of shops, restaurants, and a renowned arts community known for Varrow Arts Center and Festival which is one of the nation's top outdoor arts festivals. Maplecrest Apartments and its sign is the first thing you seen when you enter Downtown Northport. We are looking to redesign our sign, entry way and landscaping to compliment the building and character of the historic downtown.

Target Market(s)

Our apartment building is comprised of 20 apartments units with tenants who are primarily part of the local workforce, young professionals, or students at the Halverton College or other nearby institutions.

Requirements
Must have
• The name of the apartment building - Maplecrest
Phone number on the sign 205-555-0148

```html
<!DOCTYPE html>
<html lang="en">
<head>
<meta charset="utf-8">
<title>Maplecrest Entry Sign</title>
<link href="https://fonts.googleapis.com/css2?family=Oswald:wght@600;700&display=swap" rel="stylesheet">
<style>
  :root {
    --page-bg: #e9e9ec;
    --sign-white: #ffffff;
    --band-dark: #4a3a33;
    --band-mid: #6b5549;
    --photo-sky: #b9967a;
    --photo-glow: #c98a52;
    --photo-mid: #7a5a48;
    --photo-deep: #3f2f2a;
    --text-light: #ffffff;
  }
  * { margin: 0; padding: 0; box-sizing: border-box; }
  html, body {
    width: 893px;
    height: 1200px;
    overflow: hidden;
    background: var(--page-bg);
  }
  .canvas {
    position: relative;
    width: 893px;
    height: 1200px;
  }
  .sign {
    position: absolute;
    left: 46px;
    top: 440px;
    width: 800px;
    height: 320px;
    overflow: hidden;
    background: var(--sign-white);
    box-shadow: 6px 8px 14px rgba(0, 0, 0, 0.35);
  }
  .sign__photo {
    position: absolute;
    inset: 0;
    background:
      linear-gradient(180deg,
        var(--photo-sky) 0%,
        var(--photo-glow) 38%,
        var(--photo-mid) 62%,
        var(--photo-deep) 100%);
  }
  .sign__band {
    position: absolute;
    inset: 0;
    width: 800px;
    height: 320px;
  }
  .sign__phone {
    position: absolute;
    top: 12px;
    right: 44px;
    font-family: "Oswald", sans-serif;
    font-weight: 600;
    font-size: 50px;
    letter-spacing: 1px;
    line-height: 1;
    color: var(--text-light);
  }
  .sign__name {
    position: absolute;
    left: 0;
    right: 0;
    bottom: 26px;
    text-align: center;
    white-space: nowrap;
    font-family: "Oswald", sans-serif;
    font-weight: 700;
    font-size: 130px;
    line-height: 1;
    letter-spacing: 0;
    color: var(--text-light);
    text-transform: uppercase;
    text-shadow: 3px 4px 6px rgba(0, 0, 0, 0.45);
  }
</style>
</head>
<body>
  <main class="canvas">
    <section class="sign" aria-label="Maplecrest Apartments entry sign">
      <div class="sign__photo" role="img" aria-label="Warm sunset view over downtown buildings"></div>
      <svg class="sign__band" viewBox="0 0 800 320" aria-hidden="true">
        <polygon points="0,0 800,0 800,18 0,80" fill="var(--sign-white)"/>
        <polygon points="250,0 800,0 800,78 190,78" fill="var(--band-dark)"/>
        <polygon points="190,78 800,78 800,90 178,90" fill="var(--band-mid)" opacity="0.8"/>
        <polygon points="0,0 250,0 190,78 0,96" fill="var(--sign-white)"/>
      </svg>
      <p class="sign__phone">205-555-0148</p>
      <h1 class="sign__name">Maplecrest</h1>
    </section>
  </main>
</body>
</html>
```